KWT BUSINESS CARD

I'd like a new business card for the folks in my office. I recently became aware of a company that produces extra thick cards that seem to me to make excellent use of embossing. I have a logo that I like so I just need a design that uses embossing effectively, is simple and uses minimal color.

I am uploading our current logo of a tooth with a brush above it. I am also uploading another file with the words of our business. In your design please use the square version of the tooth vs. the strectched version. The original logo is the more square image but please use the words and the fonts of "Wexmoor Dental Group" and incorporate that in the design.

Industry/Entity Type

Business

Colors
ffffff

Requirements
Must have
• Logo, company name (also a part of our existing logo), employee name and title, phone number and website address. Must be simple
Nice to have
• Embossed - Maybe a solid color on the back
Should not have
• Must not be too complex or busy

```html
<!DOCTYPE html>
<html lang="en">
<head>
<meta charset="utf-8">
<title>Wexmoor Dental Group – Business Card</title>
<link rel="stylesheet" href="https://fonts.googleapis.com/css2?family=Jost:wght@400;600&display=swap">
<style>
  :root {
    --backdrop: #d7d7d7;
    --card-white: #ffffff;
    --brand-blue: #3f3f9a;
    --brand-teal: #2d6f86;
    --brand-green: #1fae4f;
    --ink: #1a1a1a;
    --title-blue: #3b3b9c;
  }
  * { box-sizing: border-box; margin: 0; padding: 0; }
  html, body { width: 1200px; height: 900px; overflow: hidden; }
  body {
    background: var(--backdrop);
    font-family: "Jost", "Century Gothic", sans-serif;
    color: var(--ink);
  }
  .card-set {
    position: absolute;
    top: 295px;
    left: 40px;
    display: flex;
    gap: 40px;
  }
  .card {
    position: relative;
    width: 540px;
    height: 310px;
    border-radius: 28px;
    overflow: hidden;
  }
  /* Front */
  .card-front { background: var(--card-white); }
  .brand-lockup {
    position: absolute;
    top: 42px;
    left: 26px;
    display: flex;
    align-items: center;
    gap: 18px;
  }
  .brand-square {
    width: 104px;
    height: 104px;
    background: var(--brand-blue);
  }
  .brand-name {
    font-weight: 600;
    font-size: 30px;
    line-height: 1.05;
    color: var(--ink);
    letter-spacing: 0.5px;
  }
  .brand-stripe {
    position: absolute;
    top: 172px;
    left: 0;
    width: 100%;
    height: 11px;
    background: linear-gradient(90deg, var(--brand-blue) 0%, var(--brand-green) 55%, var(--brand-blue) 100%);
  }
  .staff {
    position: absolute;
    top: 196px;
    left: 26px;
  }
  .staff-name { font-weight: 600; font-size: 18px; line-height: 1.2; }
  .staff-title { font-size: 15px; color: var(--title-blue); line-height: 1.3; }
  .contact-list {
    list-style: none;
    margin-top: 12px;
    font-size: 17px;
    line-height: 1.5;
  }
  .contact-list li { display: flex; align-items: center; gap: 4px; }
  .contact-icon { width: 16px; height: 16px; fill: var(--brand-blue); }
  /* Back */
  .card-back {
    background: linear-gradient(180deg, var(--brand-blue) 0%, var(--brand-teal) 50%, var(--brand-green) 100%);
    display: flex;
    align-items: center;
    justify-content: center;
  }
  .back-name {
    font-weight: 600;
    font-size: 36px;
    color: var(--card-white);
    letter-spacing: 0.5px;
  }
</style>
</head>
<body>
  <main class="card-set">
    <section class="card card-front" aria-label="Card front">
      <div class="brand-lockup">
        <div class="brand-square"></div>
        <div class="brand-name">Wexmoor<br>Dental Group</div>
      </div>
      <div class="brand-stripe"></div>
      <div class="staff">
        <p class="staff-name">Dana Lowell</p>
        <p class="staff-title">Manager</p>
        <ul class="contact-list">
          <li>
            <svg class="contact-icon" viewBox="0 0 24 24" aria-hidden="true"><path d="M6.6 10.8a15.1 15.1 0 0 0 6.6 6.6l2.2-2.2a1 1 0 0 1 1-.25 11.4 11.4 0 0 0 3.6.57 1 1 0 0 1 1 1V20a1 1 0 0 1-1 1A17 17 0 0 1 3 4a1 1 0 0 1 1-1h3.5a1 1 0 0 1 1 1c0 1.25.2 2.45.57 3.57a1 1 0 0 1-.25 1z"/></svg>
            155 010 447
          </li>
          <li>
            <svg class="contact-icon" viewBox="0 0 24 24" aria-hidden="true"><path d="M12 2a10 10 0 1 0 0 20 10 10 0 0 0 0-20zm6.9 6h-2.9a15.6 15.6 0 0 0-1.4-3.6A8 8 0 0 1 18.9 8zM12 4c.8 1.2 1.5 2.5 1.9 4h-3.8c.4-1.5 1.1-2.8 1.9-4zM4.3 14a8.2 8.2 0 0 1 0-4h3.4a16.5 16.5 0 0 0 0 4zm.8 2h2.9c.3 1.3.8 2.5 1.4 3.6A8 8 0 0 1 5.1 16zM8 8H5.1a8 8 0 0 1 4.3-3.6C8.8 5.5 8.3 6.7 8 8zm4 12c-.8-1.2-1.5-2.5-1.9-4h3.8c-.4 1.5-1.1 2.8-1.9 4zm2.3-6H9.7a14.7 14.7 0 0 1 0-4h4.6a14.7 14.7 0 0 1 0 4zm.3 5.6c.6-1.1 1.1-2.3 1.4-3.6h2.9a8 8 0 0 1-4.3 3.6zm1.7-5.6a16.5 16.5 0 0 0 0-4h3.4a8.2 8.2 0 0 1 0 4z"/></svg>
            wexmoordental.com
          </li>
        </ul>
      </div>
    </section>
    <section class="card card-back" aria-label="Card back">
      <p class="back-name">Wexmoor Dental Group</p>
    </section>
  </main>
</body>
</html>
```